Business Card Design

We Need a business card design for my company based in Tv Radio and music Productions and hunt Talent.

Industry/Entity Type

Business

Contact Information for Business Card

BrivaTune Production's, Renzo Bettafiore,Cell Phone 427 5139048
Musician, Productor, Hunt Talent. Miami Fla. www.brivatune.net Mail. renzobettafiore@kovamail.com

```html
<!DOCTYPE html>
<html lang="en">
<head>
<meta charset="utf-8">
<title>BrivaTune Production's – Business Card</title>
<link href="https://fonts.googleapis.com/css2?family=Open+Sans:wght@400;600;700&display=swap" rel="stylesheet">
<style>
  :root {
    --stage-bg: #f2f2f2;
    --card-white: #f4f4f4;
    --card-yellow: #ffd21f;
    --card-yellow-deep: #f7b900;
    --band-red: #b01e24;
    --name-red: #9e1b20;
    --text-dark: #1c1c1c;
    --role-purple: #6a2c91;
    --gold-light: #f4cb3a;
    --gold-mid: #d9a516;
    --gold-dark: #9c7413;
    --mark-gold: #f5c21b;
  }
  * { box-sizing: border-box; margin: 0; padding: 0; }
  html, body { width: 1200px; height: 900px; overflow: hidden; }
  body {
    background: var(--stage-bg);
    font-family: "Open Sans", Arial, sans-serif;
  }
  .canvas {
    position: relative;
    width: 1200px;
    height: 900px;
    display: flex;
    align-items: center;
    justify-content: center;
    gap: 40px;
  }
  .card {
    position: relative;
    width: 520px;
    height: 297px;
    border-radius: 18px;
    overflow: hidden;
    box-shadow: 0 6px 18px rgba(0,0,0,0.12);
  }
  .card-bg { position: absolute; inset: 0; width: 100%; height: 100%; }

  /* Front */
  .brand {
    position: absolute;
    display: flex;
    align-items: center;
    gap: 8px;
    font-weight: 700;
    color: var(--name-red);
    white-space: nowrap;
  }
  .brand-dot {
    border-radius: 50%;
    background: var(--mark-gold);
    flex: none;
  }
  .front .brand { left: 16px; top: 128px; font-size: 19px; }
  .front .brand-dot { width: 22px; height: 22px; }

  .holder-name {
    position: absolute;
    left: 270px;
    top: 40px;
    font-size: 21px;
    font-weight: 600;
    color: var(--name-red);
    letter-spacing: 0.3px;
    text-transform: uppercase;
  }
  .contacts {
    position: absolute;
    left: 252px;
    top: 142px;
    list-style: none;
    font-size: 16px;
    color: var(--text-dark);
    line-height: 24px;
  }
  .contacts li { display: flex; align-items: center; gap: 5px; }
  .contacts svg { width: 15px; height: 15px; flex: none; }
  .roles {
    position: absolute;
    right: 22px;
    bottom: 18px;
    font-size: 14.5px;
    font-weight: 700;
    color: var(--role-purple);
    white-space: nowrap;
  }
  .roles .sep { margin: 0 8px; }

  /* Back */
  .back-surface {
    position: absolute;
    inset: 0;
    background:
      radial-gradient(ellipse at 20% 10%, rgba(255,240,170,0.55), transparent 55%),
      linear-gradient(135deg, var(--gold-light) 0%, var(--gold-mid) 55%, var(--gold-dark) 100%);
  }
  .back .brand { right: 40px; top: 122px; font-size: 34px; gap: 12px; }
  .back .brand-dot { width: 38px; height: 38px; }
</style>
</head>
<body>
<main class="canvas">

  <section class="card front" aria-label="Business card front">
    <svg class="card-bg" viewBox="0 0 520 297" preserveAspectRatio="none" aria-hidden="true">
      <defs>
        <linearGradient id="yellowFace" x1="0" y1="0" x2="1" y2="0">
          <stop offset="0" stop-color="var(--card-yellow-deep)"/>
          <stop offset="0.4" stop-color="var(--card-yellow)"/>
          <stop offset="1" stop-color="var(--card-yellow-deep)"/>
        </linearGradient>
      </defs>
      <rect width="520" height="297" fill="url(#yellowFace)"/>
      <path d="M150 0 H258 C278 100 258 200 180 297 H168 C238 200 244 80 200 0 Z" fill="var(--band-red)"/>
      <path d="M258 0 C278 100 258 200 180 297" fill="none" stroke="#ffffff" stroke-width="3"/>
      <path d="M0 0 H200 C244 80 238 200 168 297 H0 Z" fill="var(--card-white)"/>
    </svg>

    <div class="brand"><span class="brand-dot"></span>Briva's Show</div>

    <h1 class="holder-name">Renzo Bettafiore</h1>

    <ul class="contacts">
      <li>
        <svg viewBox="0 0 24 24" aria-hidden="true"><path fill="var(--name-red)" d="M6.6 10.8a15.1 15.1 0 0 0 6.6 6.6l2.2-2.2c.3-.3.7-.4 1-.2 1.1.4 2.3.6 3.6.6.6 0 1 .4 1 1V20c0 .6-.4 1-1 1A17 17 0 0 1 3 4c0-.6.4-1 1-1h3.5c.6 0 1 .4 1 1 0 1.3.2 2.5.6 3.6.1.3 0 .7-.2 1z"/></svg>
        427 5139048
      </li>
      <li>
        <svg viewBox="0 0 24 24" aria-hidden="true"><g fill="none" stroke="var(--name-red)" stroke-width="2"><circle cx="12" cy="12" r="9"/><ellipse cx="12" cy="12" rx="4" ry="9"/><path d="M3 12h18M5 7h14M5 17h14"/></g></svg>
        www.brivatune.net
      </li>
      <li>
        <svg viewBox="0 0 24 24" aria-hidden="true"><rect x="2" y="5" width="20" height="14" rx="1.5" fill="var(--name-red)"/><path d="M3 6l9 7 9-7" fill="none" stroke="#ffd21f" stroke-width="1.8"/></svg>
        renzobettafiore@kovamail.com
      </li>
    </ul>

    <p class="roles">Musician<span class="sep">|</span>Productor<span class="sep">|</span>Hunt Talent</p>
  </section>

  <section class="card back" aria-label="Business card back">
    <div class="back-surface" role="img" aria-label="Gold background with soft swirling light lines and sparkles"></div>
    <div class="brand"><span class="brand-dot"></span>Briva's Show</div>
  </section>

</main>
</body>
</html>
```